KMR Business cards

I currently have a logo that was designed by a pixel harbor designer. I would like this to be added to the business card.

We are an innovative new start-up business offering finance solutions to the car dealership market in the UK. So our clients are quiet traditional, so are cards need to fit in, but at the same time show we are a modern online business.

Finance

```html
<!DOCTYPE html>
<html lang="en">
<head>
<meta charset="utf-8">
<title>KMR Business Cards</title>
<link rel="stylesheet" href="https://fonts.googleapis.com/css2?family=Lato:wght@400;700&display=swap">
<style>
  :root {
    --backdrop: #2b2b2b;
    --navy: #142f5e;
    --navy-deep: #0f2550;
    --paper: #f4f5f6;
    --white: #ffffff;
    --ink: #1a2f5c;
    --muted: #b9c3d6;
  }
  * { margin: 0; padding: 0; box-sizing: border-box; }
  html, body {
    width: 1200px; height: 900px; overflow: hidden;
    background: var(--backdrop);
    font-family: "Lato", sans-serif;
  }
  .stage { position: relative; width: 1200px; height: 900px; }
  .card {
    position: absolute; width: 540px; height: 308px;
    border-radius: 3px; overflow: hidden;
    box-shadow: 0 14px 30px rgba(0,0,0,.5);
  }
  .card--front { left: 70px; top: 110px; background: var(--navy); }
  .card--back { left: 590px; top: 480px; background: var(--navy); }

  .brand { display: flex; align-items: center; gap: 16px; }
  .brand__mark { flex: none; }
  .brand__name {
    font-weight: 700; line-height: 1.02; font-size: 30px;
  }
  .card--front .brand { position: absolute; left: 120px; top: 70px; color: var(--white); }
  .card--front .brand__mark circle { stroke: var(--white); }
  .tagline {
    position: absolute; left: 0; right: 0; top: 228px; text-align: center;
    color: var(--muted); font-weight: 700; font-size: 13px; letter-spacing: 4px;
  }

  .back__top {
    position: absolute; left: 0; top: 0; width: 100%; height: 160px;
    background: var(--paper);
  }
  .card--back .brand { position: absolute; left: 140px; top: 36px; color: var(--ink); }
  .card--back .brand__name { font-size: 26px; }
  .card--back .brand__mark circle { stroke: var(--ink); }
  .person { position: absolute; left: 34px; top: 232px; color: var(--white); }
  .person__name { font-weight: 700; font-size: 19px; letter-spacing: .5px; }
  .person__role { font-size: 15px; color: var(--muted); margin-top: 2px; }
  .contacts {
    position: absolute; left: 258px; top: 178px; list-style: none;
    color: var(--muted); font-size: 13px;
  }
  .contacts li { display: flex; align-items: center; gap: 10px; height: 24px; }
  .contacts svg { flex: none; }
</style>
</head>
<body>
<main class="stage">
  <section class="card card--front">
    <div class="brand">
      <svg class="brand__mark" width="72" height="72" viewBox="0 0 72 72" aria-hidden="true">
        <circle cx="36" cy="36" r="31" fill="none" stroke-width="6"/>
      </svg>
      <div class="brand__name">Keystone<br>Motor<br>Repayments</div>
    </div>
    <p class="tagline">DRIVE NOW, PAY LATER</p>
  </section>

  <section class="card card--back">
    <div class="back__top"></div>
    <div class="brand">
      <svg class="brand__mark" width="64" height="64" viewBox="0 0 64 64" aria-hidden="true">
        <circle cx="32" cy="32" r="27" fill="none" stroke-width="5"/>
      </svg>
      <div class="brand__name">Keystone<br>Motor<br>Repayments</div>
    </div>
    <div class="person">
      <p class="person__name">DANIEL MORGAN</p>
      <p class="person__role">Founder</p>
    </div>
    <ul class="contacts">
      <li>
        <svg width="14" height="14" viewBox="0 0 14 14" aria-hidden="true"><rect x="3.5" y="1" width="7" height="12" rx="1.2" fill="none" stroke="currentColor" stroke-width="1.3"/></svg>
        07700 900418
      </li>
      <li>
        <svg width="14" height="14" viewBox="0 0 14 14" aria-hidden="true"><circle cx="7" cy="7" r="6" fill="currentColor"/></svg>
        daniel.morgan_kmr
      </li>
      <li>
        <svg width="14" height="14" viewBox="0 0 14 14" aria-hidden="true"><rect x="1" y="3" width="12" height="8" fill="none" stroke="currentColor" stroke-width="1.3"/><path d="M1 3l6 5 6-5" fill="none" stroke="currentColor" stroke-width="1.3"/></svg>
        daniel.morgan@keystonemotorrepay.com
      </li>
      <li>
        <svg width="14" height="14" viewBox="0 0 14 14" aria-hidden="true"><path d="M6 8l2-2M5 6.5L3 8.5a2 2 0 0 0 2.8 2.8L7.5 9.5M9 7.5l2-2A2 2 0 0 0 8.2 2.7L6.5 4.5" fill="none" stroke="currentColor" stroke-width="1.3" stroke-linecap="round"/></svg>
        www.keystonemotorrepay.com
      </li>
    </ul>
  </section>
</main>
</body>
</html>
```